Harbor Crest Industrial Services Brochure

-Need a tri-fold brochure, please use our new website colors and theme (I will attach a screen shot as it not live yet).
- Same layout as old brochure will work but I want to match our new website design (I will attach).
-I have attached our old brochure with pen written edits
-We need to add a valve section, if you can find a better image similar to what I attache that would be great.
-I want to replace the BOP stack image with some large refiner tank image, they are usually white tanks. Ill attached a sample picture.
-I will like to replace the front cover spray gun image with sandblaster balsting the 2 large pipes.
-you can use other same images or find good replacments but they have express a fresh paint job.
-Replace structual picture with yellow/orange frame picture attached
Updates
Also add Oven Cured Coatings to Surface Coating section.
Target Market(s)
Industrial customers
Industry/Entity Type
oil & gas, refinery, heavy equipment
Look and feel

```html
<!DOCTYPE html>
<html lang="en">
<head>
<meta charset="utf-8">
<title>Harbor Crest Industrial Services – Tri-fold Brochure</title>
<link href="https://fonts.googleapis.com/css2?family=Saira+Semi+Condensed:wght@600;700;800&family=Poppins:wght@400;500;600;700&display=swap" rel="stylesheet">
<style>
:root{
  --blue:#0b4fbf;
  --blue-dark:#083f9b;
  --ink:#1a1a1a;
  --dark:#2a2a2a;
  --paper:#ffffff;
  --bg:#ffffff;
  --rule:#2b2b2b;
  --muted:#3a3a3a;
}
*{box-sizing:border-box;margin:0;padding:0}
html,body{width:1200px;height:2966px;overflow:hidden;background:var(--bg)}
body{position:relative;font-family:"Poppins",sans-serif;color:var(--ink)}
.spread{position:absolute;left:82px;width:1036px;height:800px;background:var(--paper);box-shadow:0 6px 18px rgba(0,0,0,.18)}
.spread--outside{top:600px}
.spread--inside{top:1550px}
.abs{position:absolute}
.top-rule{left:0;top:0;width:100%;height:5px;background:var(--rule)}
.top-tab{top:0;height:24px;background:var(--blue)}
.top-tab--left{left:0;width:250px;clip-path:polygon(0 0,100% 0,88% 100%,0 100%)}
.top-tab--right{right:0;width:240px;clip-path:polygon(0 0,100% 0,100% 100%,12% 100%)}
.footer{left:0;bottom:0;width:100%;height:55px;background:var(--blue);display:flex}
.footer span{flex:1;text-align:center;color:#fff;font-size:16px;line-height:55px;font-weight:500}
.heading{font-family:"Saira Semi Condensed",sans-serif;font-weight:700;text-transform:uppercase;color:var(--ink);letter-spacing:.3px}
.heading em{font-style:normal;color:var(--blue)}
.underline{height:5px}
.underline::before,.underline::after{content:"";position:absolute;top:0;height:5px;background:var(--blue)}
.underline::before{left:0;width:78%}
.underline::after{right:0;width:12%}
.ticks{list-style:none}
.ticks li{position:relative;padding-left:38px;font-size:15.5px;line-height:1.25;color:var(--ink)}
.ticks li svg{position:absolute;left:0;top:3px;width:14px;height:14px}
.photo{position:absolute}
.frame{position:absolute;border:4px solid var(--blue)}
.img-label{position:absolute;left:0;right:0;bottom:0;height:34px;background:#1d1d1d;color:#fff;text-align:center;font-family:"Saira Semi Condensed",sans-serif;font-weight:700;font-size:20px;line-height:34px;letter-spacing:.5px}
.badge{position:absolute;border:4px solid var(--blue);background:#fff}
.badge i{position:absolute;left:50%;top:50%;transform:translate(-50%,-50%);display:block;background:#c9d3e3}
.brand{display:flex;align-items:center;gap:12px}
.brand-mark{width:40px;height:40px;border:4px solid var(--blue)}
.brand-name{font-family:"Poppins",sans-serif;font-weight:600;font-size:22px;line-height:1.05;color:#3b3b3b}
.industry-list li{display:flex;align-items:center;height:33px;font-size:15.5px}
.industry-list .ico{width:30px;height:28px;border:1px solid #d8dde6;background:#eef2f8;margin-right:37px;position:relative}
.industry-list .ico::after{content:"";position:absolute;inset:8px;border-radius:3px;background:#5a79b0}
</style>
</head>
<body>
<svg width="0" height="0" style="position:absolute" aria-hidden="true">
  <symbol id="tick" viewBox="0 0 14 14">
    <rect x="1" y="2" width="10" height="10" fill="none" stroke="#0b4fbf" stroke-width="1.6"/>
    <path d="M3.5 7 L6 9.5 L13 2" fill="none" stroke="#0b4fbf" stroke-width="1.8"/>
  </symbol>
</svg>

<!-- Outside spread -->
<section class="spread spread--outside">
  <div class="abs top-rule"></div>
  <div class="abs top-tab top-tab--left"></div>
  <div class="abs top-tab top-tab--right"></div>

  <div class="abs heading" style="left:33px;top:44px;font-size:29px">Surface <em>Coatings</em></div>
  <div class="abs underline" style="left:33px;top:88px;width:275px"></div>
  <ul class="abs ticks" style="left:33px;top:108px">
    <li style="height:31.5px"><svg><use href="#tick"/></svg>Epoxy Coatings</li>
    <li style="height:31.5px"><svg><use href="#tick"/></svg>Urethane Coatings</li>
    <li style="height:31.5px"><svg><use href="#tick"/></svg>Zinc Primers</li>
    <li style="height:31.5px"><svg><use href="#tick"/></svg>Tank Linings</li>
    <li style="height:31.5px"><svg><use href="#tick"/></svg>Non-Skid Coatings</li>
    <li style="height:31.5px"><svg><use href="#tick"/></svg>High Temp Coatings</li>
    <li style="height:31.5px"><svg><use href="#tick"/></svg>Floor Coatings</li>
    <li style="height:31.5px"><svg><use href="#tick"/></svg>Fireproof Coatings</li>
    <li style="height:31.5px"><svg><use href="#tick"/></svg>Polyurea</li>
    <li style="height:31.5px"><svg><use href="#tick"/></svg>Powder Coating</li>
  </ul>
  <div class="photo" role="img" aria-label="Worker spray-coating racked parts inside a white paint booth" style="left:33px;top:455px;width:282px;height:185px;background:linear-gradient(135deg,#f4f5f7,#cfd3da 60%,#e8eaee)"></div>
  <div class="frame" style="left:55px;top:445px;width:240px;height:210px;border-top-color:transparent;border-right-width:5px"></div>
  <div class="badge" style="left:33px;top:675px;width:137px;height:50px"><i style="width:30px;height:30px;border-radius:50%"></i></div>
  <div class="badge" style="left:178px;top:675px;width:137px;height:50px"><i style="width:80px;height:18px"></i></div>

  <div class="photo" role="img" aria-label="Worker in protective suit spraying inside the surface preparation booth" style="left:345px;top:50px;width:345px;height:195px;background:linear-gradient(120deg,#cfd5de,#f1f3f6 50%,#aeb6c2)"></div>
  <div class="abs" style="left:380px;top:240px;width:275px;height:46px;background:var(--blue);color:#fff;text-align:center;font-family:'Saira Semi Condensed',sans-serif;font-weight:700;font-size:20px;line-height:46px;border:3px solid #fff">SURFACE PREAPRING AREA</div>
  <ul class="abs ticks" style="left:375px;top:308px;width:290px">
    <li style="font-size:14px;margin-bottom:18px"><svg><use href="#tick"/></svg>1- BLAST ENCLOSURE<br>75 WX60 LX28°H<br>(4,500SAFT).</li>
    <li style="font-size:14px"><svg><use href="#tick"/></svg>5+ ACRES OF OUTDOOR BLAST AREA FOR ITEMS IN EXCESS OF 75 IN LENGTH OR WIDTH</li>
  </ul>
  <div class="abs" style="left:376px;top:470px;width:284px;height:50px;border:4px solid var(--blue);color:var(--blue);text-align:center;font-family:'Saira Semi Condensed',sans-serif;font-weight:700;font-size:20px;line-height:42px">COATING AREAS</div>
  <ul class="abs ticks" style="left:375px;top:550px;width:290px">
    <li style="font-size:14px;height:31px"><svg><use href="#tick"/></svg>1 - LARGE SPRAY BOOTH 50° X 120°</li>
    <li style="font-size:14px;height:31px"><svg><use href="#tick"/></svg>2 - LARGE SPRAY BOOTHS 75° X 60°</li>
    <li style="font-size:14px;height:31px"><svg><use href="#tick"/></svg>1 - MID SIZE BOOTH 35 X 30°</li>
    <li style="font-size:14px;height:50px"><svg><use href="#tick"/></svg>20,000 SOFT OF TOTAL<br>COATING BOOTH</li>
    <li style="font-size:14px"><svg><use href="#tick"/></svg>7 ACRES OF LAYDOWN YARD</li>
  </ul>

  <div class="abs brand" style="left:725px;top:50px">
    <div class="brand-mark"></div>
    <div class="brand-name">Harbor Crest<br>Industrial Services</div>
  </div>
  <div class="photo" role="img" aria-label="Sandblaster blasting the inside of two large pipes in a dust cloud" style="left:712px;top:158px;width:292px;height:310px;background:radial-gradient(circle at 50% 55%,#f7f3ee,#d8cbbb 60%,#a98c6e)"></div>
  <div class="frame" style="left:710px;top:155px;width:297px;height:315px;border-top-color:transparent;border-right-color:transparent"></div>
  <div class="frame" style="left:930px;top:155px;width:77px;height:315px;border-left:none;border-bottom:none"></div>
  <div class="abs" style="left:700px;top:496px;width:336px;text-align:center">
    <div style="font-size:35px;font-weight:400;line-height:1.05">COMMITED TO</div>
    <div class="heading" style="font-family:'Poppins',sans-serif;font-weight:700;font-size:60px;line-height:1;color:var(--blue)">QUALITY</div>
    <div style="font-size:31px;font-weight:700;line-height:1.15">&amp; COMPLIANCE</div>
    <div style="width:90px;height:6px;background:var(--ink);margin:20px auto 22px"></div>
    <div style="font-size:16px;line-height:1.2">At Harbor Crest Inc.</div>
    <div style="font-size:10.5px;line-height:1.35">We Have Only One Purpose — Satisfying YouAnd<br>Your Needs For Protective Coating Services.</div>
  </div>

  <div class="abs footer"><span>www.harborcrestinc.com</span><span>www.harborcrestinc.com</span><span>www.harborcrestinc.com</span></div>
</section>

<!-- Inside spread -->
<section class="spread spread--inside">
  <div class="abs top-rule"></div>
  <div class="abs top-tab top-tab--left"></div>
  <div class="abs top-tab top-tab--right"></div>

  <div class="abs heading" style="left:33px;top:44px;font-size:29px">Industries <em>We Serve</em></div>
  <div class="abs underline" style="left:33px;top:88px;width:275px"></div>
  <ul class="abs ticks industry-list" style="left:33px;top:112px">
    <li><span class="ico"></span>Structural Steel</li>
    <li><span class="ico"></span>Critical components</li>
    <li><span class="ico"></span>Processing &amp; Refining</li>
    <li><span class="ico"></span>Waste Management</li>
    <li><span class="ico"></span>Subsea Structures</li>
    <li><span class="ico"></span>Skid Packages</li>
    <li><span class="ico"></span>Heavy Equipment</li>
    <li><span class="ico"></span>Transportation</li>
    <li><span class="ico"></span>Tanks</li>
    <li><span class="ico"></span>Valves</li>
  </ul>
  <div class="photo" role="img" aria-label="Large white refinery storage tanks under a pale sky" style="left:33px;top:465px;width:282px;height:265px;background:linear-gradient(180deg,#c9d1dc,#f2f3f5 45%,#dfe2e6)">
    <div class="img-label" style="font-family:'Poppins',sans-serif;font-weight:400;font-size:17px;height:40px;line-height:40px">TANKS</div>
  </div>
  <div class="frame" style="left:33px;top:465px;width:282px;height:265px;border-right-width:5px"></div>

  <div class="photo" role="img" aria-label="Freshly painted white structural steel loaded on a flatbed truck" style="left:375px;top:50px;width:283px;height:158px;background:linear-gradient(180deg,#c7ccd3,#eef0f2 55%,#7d7f82)"><div class="img-label">STRUCTURAL</div></div>
  <div class="photo" role="img" aria-label="Blue pump and motor assemblies with fresh paint" style="left:375px;top:225px;width:283px;height:158px;background:linear-gradient(135deg,#1e4ea8,#3a72d0 50%,#173c80)"><div class="img-label">ASSEMBLIES</div></div>
  <div class="photo" role="img" aria-label="Rows of freshly coated grey valves on pallets" style="left:375px;top:397px;width:283px;height:158px;background:linear-gradient(135deg,#9a9ea4,#d2d4d7 50%,#8c8f94)"><div class="img-label">VALVES</div></div>
  <div class="photo" role="img" aria-label="Red heavy haul trailer with multiple wheel axles" style="left:375px;top:568px;width:283px;height:158px;background:linear-gradient(180deg,#c42727,#8e1a1a 55%,#6b6b6b)"><div class="img-label">HEAVY EQIPMENT</div></div>

  <div class="abs heading" style="left:722px;top:48px;font-size:27px;line-height:1.1">Lifting capacity of<br><em style="font-size:29px">125,000 LBS.</em></div>
  <div class="photo" role="img" aria-label="Orange painted steel lifting frame on a gravel yard" style="left:718px;top:127px;width:283px;height:213px;background:linear-gradient(180deg,#b8c0c8,#dfe3e7 40%,#e07a1f 62%,#8d8a85)"></div>
  <div class="abs heading" style="left:722px;top:355px;font-size:25px;line-height:.95">Inhouse and field<br><em>Services</em></div>
  <div class="abs underline" style="left:722px;top:410px;width:240px"></div>
  <ul class="abs ticks" style="left:722px;top:428px">
    <li style="font-size:14.5px;height:24px"><svg><use href="#tick"/></svg>24 hours a day, 7 days a week</li>
    <li style="font-size:14.5px"><svg><use href="#tick"/></svg>Mobile equipment on standby</li>
  </ul>
  <div class="abs heading" style="left:722px;top:493px;font-size:25px">Easy <em>Acces to</em></div>
  <div class="abs underline" style="left:722px;top:528px;width:240px"></div>
  <ul class="abs ticks" style="left:722px;top:545px">
    <li style="font-size:14.5px;height:23.5px"><svg><use href="#tick"/></svg>Beltway 8</li>
    <li style="font-size:14.5px;height:23.5px"><svg><use href="#tick"/></svg>Houston Ports</li>
    <li style="font-size:14.5px"><svg><use href="#tick"/></svg>JFK and Hobby Airports</li>
  </ul>
  <div class="abs heading" style="left:722px;top:630px;width:276px;height:50px;border:4px solid var(--blue);border-top-color:transparent;font-size:26px;line-height:42px;padding-left:14px">Need a <em>Quote?</em></div>
  <div class="abs" style="left:722px;top:688px;font-family:'Saira Semi Condensed',sans-serif;font-weight:700;font-size:23px;display:flex;align-items:center;gap:6px">
    <svg width="14" height="14" viewBox="0 0 14 14" aria-hidden="true"><path d="M3 1 L5.5 4 L4 5.5 Q5.5 8.5 8.5 10 L10 8.5 L13 11 L11 13 Q5 12.5 1 3 Z" fill="#0b4fbf"/></svg>
    Office: 281-555-0148
  </div>
  <div class="abs" style="left:722px;top:716px;font-size:13px;font-weight:700;display:flex;align-items:center;gap:6px">
    <svg width="12" height="15" viewBox="0 0 12 15" aria-hidden="true"><path d="M6 14 C2 9 1 7 1 5 A5 5 0 0 1 11 5 C11 7 10 9 6 14 Z" fill="none" stroke="#0b4fbf" stroke-width="1.8"/><circle cx="6" cy="5" r="1.7" fill="#0b4fbf"/></svg>
    2200 Cedar Bend Rd, Houston, TX 77044
  </div>

  <div class="abs footer"><span>www.harborcrestinc.com</span><span>www.harborcrestinc.com</span><span>www.harborcrestinc.com</span></div>
</section>
</body>
</html>
```